Web Site for Strategy and Technology Consulting Company

We are looking for a website design that engages potential customers to understand our services and contact us. In this contest, we are looking for a homepage design, but the winning designer will be favored for the design of some of the more complicated interior pages of the site. An additional contest (or contests) for these pages will be added soon.

PLATROM AND RESPONSIVE DESIGN
The site will be implemented in WordPress using the Elementor page builder.
We are looking for a design that will look good on phones are well as laptop browsers.

UPLOADED FILES INCLUDE:
1a A wireframe of the homepage we are looking for. The Uploaded PDF also includes a draft of the text proposed for the homepage. Designers are free to go beyond the wireframe, but all elements of the wireframe should be included.
1b A Word document with the draft text of the homepage.
2a-d The Norvalith logo. Two versions are included – a dark version which works well against a light background, and a light version which works well against a dark background.
3 The Norvalith color palette with HEX and RGB values. Designers are not limited to this palette, but colors should be complementary.
4 A draft of the homepage menu
5 Service sheets with information on the services we provide

MORE ABOUT NORVALITH
Norvalith is a consulting company focused on transforming businesses through software. Our tagline, “Transformation Delivered,” recognizes the gap business often have between business transformation and the software they end up with. By listening to our customers and understanding their vision and where they are, we help get our customers where they want to go.

We increase our capability by working with many consultants and partners, allowing us to provide our customers with the best people and the software that best suits them.

Industry/Entity Type

Consulting

Number of Pages Required

1 page

Font styles to use
Sans Serif

Requirements
Must have
• the content represented on the wireframe uploaded
Nice to have
• interactive features, such as roll-over icons that reveal additional information

```html
<!DOCTYPE html>
<html lang="en">
<head>
<meta charset="utf-8">
<title>Norvalith — Transformation Delivered</title>
<link href="https://fonts.googleapis.com/css2?family=Heebo:wght@400;500;600;700;800&display=swap" rel="stylesheet">
<style>
:root{
  --blue:#245f99;
  --blue-dark:#1d4f82;
  --yellow:#e3b710;
  --ink:#111418;
  --text:#4b5563;
  --light:#eef3f8;
  --card:#eef1f5;
  --footer:#2b3445;
  --white:#ffffff;
}
*{margin:0;padding:0;box-sizing:border-box}
html,body{width:1200px;height:3115px;overflow:hidden;background:var(--white)}
body{font-family:"Heebo",Arial,sans-serif;color:var(--ink);position:relative}
.abs{position:absolute}
.btn{position:absolute;display:flex;align-items:center;justify-content:space-between;background:var(--yellow);color:var(--ink);font-weight:500;font-size:15px;border-radius:6px;padding:0 8px 0 22px}
.btn .arrow{width:26px;height:26px;border-radius:50%;background:var(--blue);display:flex;align-items:center;justify-content:center}
.accent-blue{color:var(--blue)}
.accent-yellow{color:var(--yellow)}

/* header */
.site-header{top:0;left:0;width:1200px;height:63px;background:var(--blue)}
.logo-box{top:0;left:0;width:315px;height:63px;background:var(--white);display:flex;align-items:center;padding-left:60px;gap:8px}
.logo-mark{width:12px;height:12px;background:var(--blue);border-radius:50%}
.logo-text{font-size:40px;font-weight:500;color:#5b6472;letter-spacing:.5px}
.main-nav{top:20px;left:403px;display:flex;gap:36px;color:var(--white);font-size:15px;font-weight:500}
.main-nav span{display:flex;align-items:center;gap:8px}
.header-cta{top:13px;left:986px;width:154px;height:38px}

/* hero */
.hero{top:63px;left:0;width:1200px;height:650px;background:linear-gradient(100deg,#06080b 0%,#0c1218 45%,#1c3a44 70%,#2e5660 85%,#203038 100%)}
.hero-title{top:145px;left:60px;font-size:50px;font-weight:700;color:var(--white)}
.hero-copy{top:212px;left:62px;width:625px;color:var(--white);font-size:14.5px;line-height:23px}
.hero-list{top:313px;left:60px;color:var(--white);font-size:14.5px;line-height:23px;list-style:none}
.hero-list li{display:flex;gap:14px;margin-bottom:8px;width:520px}
.hero-list svg{flex:none;margin-top:3px}
.hero-btn{top:471px;left:60px;width:142px;height:36px}

/* services */
.svc-card{position:absolute;width:182px;height:185px;background:var(--card);text-align:center;padding:18px 10px 0}
.svc-card h3{font-size:16.5px;font-weight:600;line-height:24px;margin-top:6px}
.svc-card p{font-size:13.5px;line-height:23px;color:var(--text);margin-top:4px}
.svc-card.active{background:var(--blue)}
.svc-card.active h3,.svc-card.active p{color:var(--white)}
.section-title{font-size:39px;font-weight:700;line-height:49px}
.body-copy{font-size:14px;line-height:22.5px;color:var(--text)}

/* people */
.people-bg{top:1255px;left:0;width:1200px;height:540px;background:linear-gradient(160deg,#f4f7fb,#e9f0f7)}
.people-photo{top:1331px;left:123px;width:340px;height:376px;background:linear-gradient(135deg,#c9b9a4,#8b7a6a 50%,#3f4652)}
.dots{background-image:radial-gradient(var(--blue) 1.4px,transparent 1.6px);background-size:10px 10px}
.check-row{display:flex;gap:18px;margin-bottom:8px}
.check-row svg{flex:none;margin-top:3px}

/* testimonials */
.t-card{position:absolute;top:1951px;width:435px;height:231px;background:var(--white);border:1px solid #d6e1ee;border-top:3px solid var(--yellow);border-radius:0 0 10px 10px;padding:32px 36px 0}
.t-card p{font-size:13.5px;line-height:22.5px;color:var(--text)}
.stars{display:flex;align-items:center;gap:3px;margin-top:10px;font-size:13px;font-weight:500}
.stars b{margin-left:8px;font-weight:500}
.avatar{position:absolute;width:76px;height:76px;border-radius:50%;background:linear-gradient(160deg,#e4e1dc,#b9aa99)}
.t-name{position:absolute;font-size:16px;font-weight:600;color:var(--yellow)}
.t-company{position:absolute;font-size:13px;color:#333}
.slider-arrow{position:absolute;top:2037px;width:42px;height:42px;border-radius:50%;display:flex;align-items:center;justify-content:center}

/* partners */
.partner{position:absolute;top:2433px;width:203px;height:145px;background:var(--light);display:flex;align-items:center;justify-content:center;gap:10px;font-size:30px;font-weight:500;color:#2b2f38}
.partner.active{background:var(--blue);color:var(--white)}
.partner i{width:26px;height:26px;border-radius:50%;background:var(--yellow);display:block}
.partner.active i{background:var(--white)}
.pager{top:2608px;left:517px;display:flex;gap:6px}
.pager span{width:29px;height:4px;background:var(--blue);display:block}

/* footer */
.footer-body{top:2800px;left:0;width:1200px;height:315px;background:var(--footer)}
.footer-col{position:absolute;top:2869px;color:var(--white);font-size:13px;line-height:19px}
.footer-col h4{color:var(--yellow);font-size:16px;font-weight:600;margin-bottom:12px}
.footer-links a{display:block;color:var(--white);text-decoration:none;font-size:13px;margin-bottom:12px}
.contact-row{display:flex;gap:14px;margin-bottom:14px}
.social{display:flex;gap:6px}
.social span{width:34px;height:34px;border-radius:50%;border:1.5px solid var(--white);display:block}
.social span.on{background:var(--yellow);border-color:var(--yellow)}
.copyright{top:3090px;left:0;width:1200px;text-align:center;color:var(--white);font-size:12.5px}
</style>
</head>
<body>

<!-- Header -->
<header class="abs site-header">
  <div class="abs logo-box"><span class="logo-mark"></span><span class="logo-text">Norvalith</span></div>
  <nav class="abs main-nav">
    <span>About Us <svg width="12" height="8" viewBox="0 0 12 8"><path d="M1 1l5 5 5-5" stroke="#fff" stroke-width="2" fill="none"/></svg></span>
    <span>Services <svg width="12" height="8" viewBox="0 0 12 8"><path d="M1 1l5 5 5-5" stroke="#fff" stroke-width="2" fill="none"/></svg></span>
    <span>Insights <svg width="12" height="8" viewBox="0 0 12 8"><path d="M1 1l5 5 5-5" stroke="#fff" stroke-width="2" fill="none"/></svg></span>
    <span>Join Us <svg width="12" height="8" viewBox="0 0 12 8"><path d="M1 1l5 5 5-5" stroke="#fff" stroke-width="2" fill="none"/></svg></span>
  </nav>
  <a class="btn header-cta">Contact Us <span class="arrow"><svg width="14" height="12" viewBox="0 0 14 12"><path d="M1 6h11M7 1l5 5-5 5" stroke="#fff" stroke-width="2" fill="none"/></svg></span></a>
</header>

<!-- Hero -->
<section class="abs hero" role="img" aria-label="Photo of a woman analysing data dashboards on a monitor in a dark office"></section>
<h1 class="abs hero-title">Transformation <span class="accent-yellow">Delivered.</span></h1>
<p class="abs hero-copy">We do more for our customers than implement software. We listen. We work to understand where they are in their transformation journey and where they want to go. We partner with them to clear the roadblocks that stand in their way, ensuring they reach their destination. At Norvalith, we:</p>
<ul class="abs hero-list">
  <li><svg width="18" height="18" viewBox="0 0 18 18"><circle cx="9" cy="9" r="7.5" stroke="#e3b710" stroke-width="1.6" fill="none" stroke-dasharray="38 6"/><path d="M5.5 9l2.5 2.5 4.5-5" stroke="#e3b710" stroke-width="1.6" fill="none"/></svg>Focus on business value, with an emphasis on delivering value quickly.</li>
  <li><svg width="18" height="18" viewBox="0 0 18 18"><circle cx="9" cy="9" r="7.5" stroke="#e3b710" stroke-width="1.6" fill="none" stroke-dasharray="38 6"/><path d="M5.5 9l2.5 2.5 4.5-5" stroke="#e3b710" stroke-width="1.6" fill="none"/></svg>Meet our customers where they are without backing them up to the beginning of their journey.</li>
  <li><svg width="18" height="18" viewBox="0 0 18 18"><circle cx="9" cy="9" r="7.5" stroke="#e3b710" stroke-width="1.6" fill="none" stroke-dasharray="38 6"/><path d="M5.5 9l2.5 2.5 4.5-5" stroke="#e3b710" stroke-width="1.6" fill="none"/></svg>Provide a wide range of services, from strategy to product support.</li>
  <li><svg width="18" height="18" viewBox="0 0 18 18"><circle cx="9" cy="9" r="7.5" stroke="#e3b710" stroke-width="1.6" fill="none" stroke-dasharray="38 6"/><path d="M5.5 9l2.5 2.5 4.5-5" stroke="#e3b710" stroke-width="1.6" fill="none"/></svg>Commit to our customer’s long-term success.</li>
</ul>
<a class="btn hero-btn">Our Story <span class="arrow"><svg width="14" height="12" viewBox="0 0 14 12"><path d="M1 6h11M7 1l5 5-5 5" stroke="#fff" stroke-width="2" fill="none"/></svg></span></a>

<svg class="abs" style="top:560px;left:0" width="1200" height="160" viewBox="0 0 1200 160">
  <path d="M0 82 C 180 10, 420 0, 620 62 S 1000 190, 1200 62 L1200 160 L0 160 Z" fill="#fff"/>
  <path d="M0 82 C 180 10, 420 0, 620 62 S 1000 190, 1200 62" stroke="#e3b710" stroke-width="5" fill="none"/>
  <circle cx="600" cy="64" r="30" fill="#fff" stroke="#e6e6e6"/>
  <rect x="591" y="48" width="18" height="30" rx="9" stroke="#245f99" stroke-width="2" fill="none"/>
  <line x1="600" y1="54" x2="600" y2="60" stroke="#245f99" stroke-width="2"/>
</svg>

<!-- Services -->
<div class="svc-card" style="left:60px;top:821px">
  <svg width="50" height="48" viewBox="0 0 50 48" fill="none" stroke="#245f99" stroke-width="1.8"><rect x="4" y="4" width="38" height="28"/><path d="M12 26v-6M18 26v-10M24 26v-8"/><circle cx="32" cy="22" r="7"/><path d="M37 27l7 7M14 32l-4 12M32 32l4 12"/></svg>
  <h3>Business<br>Transformation</h3>
  <p>Define and execute your strategy.</p>
</div>
<div class="svc-card" style="left:249px;top:765px">
  <svg width="50" height="48" viewBox="0 0 50 48" fill="none" stroke="#245f99" stroke-width="1.8"><rect x="5" y="4" width="40" height="30" rx="2"/><path d="M5 10h40"/><circle cx="17" cy="22" r="6"/><path d="M17 16v6h6M28 28v-6M33 28v-10M38 28v-7M20 40h10"/></svg>
  <h3>BI and Data</h3>
  <p>Discover, connect, and trust your data.</p>
</div>
<div class="svc-card" style="left:440px;top:852px">
  <svg width="50" height="48" viewBox="0 0 50 48" fill="none" stroke="#245f99" stroke-width="1.8"><circle cx="25" cy="24" r="10"/><circle cx="25" cy="5" r="3"/><circle cx="25" cy="43" r="3"/><circle cx="7" cy="14" r="3"/><circle cx="43" cy="14" r="3"/><circle cx="7" cy="34" r="3"/><circle cx="43" cy="34" r="3"/><path d="M25 8v6M25 34v6M10 15l7 4M40 15l-7 4M10 33l7-4M40 33l-7-4"/></svg>
  <h3>Building the Right<br>Team of People</h3>
  <p>Hire resources for your transformation journey.</p>
</div>
<div class="svc-card active" style="left:249px;top:959px">
  <svg width="50" height="48" viewBox="0 0 50 48" fill="none" stroke="#fff" stroke-width="1.8"><rect x="4" y="6" width="42" height="30" rx="2"/><circle cx="14" cy="16" r="6"/><path d="M24 30v-6M30 30v-10M36 30v-14M14 36v6M8 42h12"/></svg>
  <h3>ERP<br>Implementations</h3>
  <p>Define and execute your strategy.</p>
</div>
<div class="svc-card" style="left:60px;top:1015px">
  <svg width="50" height="48" viewBox="0 0 50 48" fill="none" stroke="#245f99" stroke-width="1.8"><rect x="6" y="10" width="32" height="34" rx="2"/><rect x="24" y="3" width="22" height="12" rx="2"/><circle cx="16" cy="24" r="5"/><path d="M26 22h8M26 28h8M12 36h22"/></svg>
  <h3>CRM<br>Implementations</h3>
  <p>Take your relationships to the next level.</p>
</div>

<h2 class="abs section-title" style="top:807px;left:668px">Transformation<br><span class="accent-blue">Supported by Technology</span></h2>
<p class="abs body-copy" style="top:914px;left:668px;width:470px">During our early years, Norvalith focused only on business transformation. We came to realize that successful transformation often depended on quality software implementations, and often more than one. Now we focus on five things, the five things most businesses need to reach their goals.</p>
<a class="btn" style="top:1045px;left:668px;width:162px;height:39px">How We Work <span class="arrow"><svg width="14" height="12" viewBox="0 0 14 12"><path d="M1 6h11M7 1l5 5-5 5" stroke="#fff" stroke-width="2" fill="none"/></svg></span></a>

<!-- People -->
<div class="abs people-bg"></div>
<svg class="abs" style="top:1230px;left:0" width="1200" height="130" viewBox="0 0 1200 130">
  <path d="M0 95 C 200 160, 450 130, 620 75 C 800 15, 1020 -10, 1200 110 L1200 0 L0 0 Z" fill="#fff"/>
  <path d="M0 95 C 200 160, 450 130, 620 75 C 800 15, 1020 -10, 1200 110" stroke="#e3b710" stroke-width="4" fill="none"/>
</svg>
<div class="abs dots" style="top:1298px;left:90px;width:86px;height:66px"></div>
<div class="abs" style="top:1394px;left:60px;width:75px;height:200px;background:var(--blue)"></div>
<div class="abs people-photo" role="img" aria-label="Photo of a smiling team working together at a laptop in an office"></div>
<div class="abs dots" style="top:1655px;left:406px;width:84px;height:68px"></div>

<h2 class="abs section-title" style="top:1397px;left:575px;font-size:48px;line-height:56px">It’s the <span class="accent-blue">People</span></h2>
<p class="abs body-copy" style="top:1461px;left:575px;width:560px">The world has changed in the past twenty years. The people you need might not all work for one company. Our clients want the best resources, available quickly. That’s why, in addition to our team of experts, we partner with:</p>
<div class="abs body-copy" style="top:1541px;left:573px;width:560px">
  <div class="check-row"><svg width="18" height="18" viewBox="0 0 18 18"><circle cx="9" cy="9" r="7.5" stroke="#245f99" stroke-width="1.6" fill="none" stroke-dasharray="38 6"/><path d="M5.5 9l2.5 2.5 4.5-5" stroke="#245f99" stroke-width="1.6" fill="none"/></svg><span>A large network of expert consultants who are the best at what they do,</span></div>
  <div class="check-row"><svg width="18" height="18" viewBox="0 0 18 18"><circle cx="9" cy="9" r="7.5" stroke="#245f99" stroke-width="1.6" fill="none" stroke-dasharray="38 6"/><path d="M5.5 9l2.5 2.5 4.5-5" stroke="#245f99" stroke-width="1.6" fill="none"/></svg><span>Service providers all over the world to provide the resources and value that are right for you, available 24 x 7.</span></div>
</div>
<p class="abs body-copy" style="top:1628px;left:575px;width:560px">People are invariably at the center of our customer’s success. Find out how we can add our experts to yours.</p>
<a class="btn" style="top:1697px;left:575px;width:175px;height:37px">Meet Our Team <span class="arrow"><svg width="14" height="12" viewBox="0 0 14 12"><path d="M1 6h11M7 1l5 5-5 5" stroke="#fff" stroke-width="2" fill="none"/></svg></span></a>

<!-- Testimonials -->
<p class="abs" style="top:1856px;left:0;width:1200px;text-align:center;font-size:14px;color:#333">Testimonials</p>
<h2 class="abs section-title" style="top:1882px;left:0;width:1200px;text-align:center">What Our <span class="accent-blue">Client Are Says...</span></h2>

<div class="slider-arrow" style="left:66px;border:1.5px solid #222"><svg width="18" height="14" viewBox="0 0 18 14"><path d="M17 7H2M8 1L2 7l6 6" stroke="#222" stroke-width="2" fill="none"/></svg></div>
<div class="slider-arrow" style="left:1080px;background:var(--yellow)"><svg width="18" height="14" viewBox="0 0 18 14"><path d="M1 7h15M10 1l6 6-6 6" stroke="#222" stroke-width="2" fill="none"/></svg></div>

<div class="t-card" style="left:151px">
  <p>Lorem Ipsum is simply dummy text of the printing and typesetting industry. Lorem Ipsum has been the industry's standard dummy text ever since the 1500s, when an unknown printer took a galley of type and scrambled it to make a type specimen book. It has survived not only five centuries.</p>
  <div class="stars"><svg width="100" height="18" viewBox="0 0 100 18" fill="#e3b710"><path id="star" d="M9 1l2.4 5 5.4.6-4 3.7 1.1 5.4L9 13l-4.9 2.7 1.1-5.4-4-3.7 5.4-.6z"/><use href="#star" x="20"/><use href="#star" x="40"/><use href="#star" x="60"/><use href="#star" x="80"/></svg><b>4.9 reviews</b></div>
</div>
<div class="t-card" style="left:615px">
  <p>Lorem Ipsum is simply dummy text of the printing and typesetting industry. Lorem Ipsum has been the industry's standard dummy text ever since the 1500s, when an unknown printer took a galley of type and scrambled it to make a type specimen book. It has survived not only five centuries.</p>
  <div class="stars"><svg width="100" height="18" viewBox="0 0 100 18" fill="#e3b710"><use href="#star"/><use href="#star" x="20"/><use href="#star" x="40"/><use href="#star" x="60"/><use href="#star" x="80"/></svg><b>4.9 reviews</b></div>
</div>

<div class="avatar" style="left:163px;top:2208px" role="img" aria-label="Client portrait photo"></div>
<span class="t-name" style="left:256px;top:2222px">Daniel Reyes</span>
<span class="t-company" style="left:256px;top:2248px">Company Name</span>
<div class="avatar" style="left:625px;top:2208px;background:linear-gradient(160deg,#e8edf2,#a9b8c6)" role="img" aria-label="Client portrait photo"></div>
<span class="t-name" style="left:718px;top:2222px">Daniel Reyes</span>
<span class="t-company" style="left:718px;top:2248px">Company Name</span>

<!-- Partners -->
<h2 class="abs section-title" style="top:2368px;left:0;width:1200px;text-align:center">Transformation <span class="accent-blue">Supported by Technology</span></h2>
<div class="partner" style="left:60px"><i></i>Voltrix</div>
<div class="partner active" style="left:279px"><i></i>Searlo</div>
<div class="partner" style="left:498px"><i></i>Ovana</div>
<div class="partner" style="left:717px"><i></i>Ideon</div>
<div class="partner" style="left:936px"><i></i>Hexel</div>
<div class="abs pager"><span></span><span style="background:var(--yellow)"></span><span></span><span></span><span></span></div>

<!-- Footer -->
<svg class="abs" style="top:2660px;left:0" width="1200" height="150" viewBox="0 0 1200 150">
  <path d="M0 86 C 220 170, 420 150, 640 85 C 840 25, 1050 -10, 1200 80 L1200 150 L0 150 Z" fill="#2b3445"/>
  <path d="M0 86 C 220 170, 420 150, 640 85 C 840 25, 1050 -10, 1200 80" stroke="#e3b710" stroke-width="4" fill="none"/>
</svg>
<div class="abs footer-body"></div>

<div class="footer-col" style="left:60px;top:2854px;width:240px">
  <div style="display:flex;align-items:center;gap:8px;margin-bottom:10px"><span class="logo-mark" style="background:var(--yellow)"></span><span style="font-size:44px;font-weight:500;color:#fff;line-height:48px">Norvalith</span></div>
  <p>Lorem Ipsum is simply dummy text of the printing and typesetting industry. Lorem Ipsum has been the industry's.</p>
</div>
<div class="footer-col footer-links" style="left:339px">
  <h4>Quick Links:</h4>
  <a>About Us</a><a>Services</a><a>Insights</a><a>Join Us</a><a>Contact Us</a>
</div>
<div class="footer-col" style="left:613px;width:250px">
  <h4>Contact Us:</h4>
  <div class="contact-row"><svg width="16" height="18" viewBox="0 0 16 18"><path d="M8 17s6-6 6-10A6 6 0 0 0 2 7c0 4 6 10 6 10z" stroke="#e3b710" stroke-width="1.8" fill="none"/><circle cx="8" cy="7" r="2" fill="#e3b710"/></svg><span>123, Lorem Ipsum is simply dummy text of the printing.</span></div>
  <div class="contact-row"><svg width="16" height="16" viewBox="0 0 16 16"><path d="M3 1l3 3-2 2c1 2 3 4 5 5l2-2 3 3-2 3C6 15 1 10 1 3z" stroke="#e3b710" stroke-width="1.6" fill="none"/></svg><b style="font-weight:600">123 456 7890</b></div>
  <div class="contact-row"><svg width="18" height="14" viewBox="0 0 18 14"><rect x="1" y="1" width="16" height="12" fill="#e3b710"/><path d="M1 1l8 6 8-6" stroke="#2b3445" stroke-width="1.4" fill="none"/></svg><span>info@norvalith.com</span></div>
</div>
<div class="footer-col" style="left:890px">
  <h4>Connect With Us:</h4>
  <div class="social" aria-label="Social media links"><span></span><span></span><span class="on"></span><span></span></div>
</div>
<p class="abs copyright">© 2023 Copyright. Norvalith. All Right Reserved.</p>

</body>
</html>
```